SHG business cards

design a business card

(Generators . Lighting Towers . De-watering Pumps . Compressors) put under the logo please. my details are Marek Oyelaran (Director) 0461527308 silverpinehaulgroup@postvane.com

```html
<!DOCTYPE html>
<html lang="en">
<head>
<meta charset="utf-8">
<title>SHG Business Cards</title>
<link href="https://fonts.googleapis.com/css2?family=Montserrat:wght@400;500;700&display=swap" rel="stylesheet">
<style>
  :root {
    --backdrop: #2b2b2b;
    --card: #151515;
    --ink-light: #f2f2f2;
    --ink-muted: #8c8c8c;
    --gold: #e4a33a;
    --rule: #5a5a5a;
  }
  * { margin: 0; padding: 0; box-sizing: border-box; }
  html, body {
    width: 1200px; height: 689px; overflow: hidden;
    background: var(--backdrop);
    font-family: "Montserrat", sans-serif;
  }
  .canvas {
    position: relative; width: 1200px; height: 689px;
    display: flex; align-items: center; justify-content: center; gap: 40px;
  }
  .card {
    width: 540px; height: 309px;
    background: var(--card);
    border-radius: 22px;
    box-shadow: 0 18px 40px rgba(0,0,0,.45);
    display: flex; flex-direction: column; align-items: center; justify-content: center;
    text-align: center;
  }
  .brand {
    display: flex; align-items: center; gap: 12px;
  }
  .brand-mark {
    width: 22px; height: 22px; border-radius: 50%;
  }
  .brand-name {
    font-weight: 700; font-size: 26px; letter-spacing: 1.5px; text-transform: uppercase;
  }
  .brand-rule {
    width: 360px; height: 1px; background: var(--rule); margin: 12px 0 0;
  }
  .card--front .brand-name { color: var(--ink-muted); }
  .card--front .brand-mark { background: var(--ink-muted); }
  .services {
    margin-top: 44px; color: var(--ink-light); font-size: 14px; letter-spacing: .3px;
  }
  .card--back .brand-name { color: var(--gold); font-size: 22px; }
  .card--back .brand-mark { background: var(--gold); width: 18px; height: 18px; }
  .card--back .brand-rule { width: 320px; }
  .person-name {
    margin-top: 22px; color: var(--gold); font-weight: 700; font-size: 24px;
  }
  .person-role {
    margin-top: 4px; color: var(--ink-light); font-size: 14px;
  }
  .contact-icons {
    display: flex; gap: 8px; margin-top: 14px;
  }
  .contact-icon {
    width: 22px; height: 22px; border-radius: 50%; background: var(--gold);
    display: flex; align-items: center; justify-content: center;
  }
  .contact-line {
    color: var(--ink-light); font-size: 14px; margin-top: 8px; letter-spacing: .3px;
  }
  .contact-line:first-of-type { margin-top: 14px; }
</style>
</head>
<body>
<main class="canvas">
  <section class="card card--front">
    <div class="brand">
      <span class="brand-mark"></span>
      <span class="brand-name">Silverpine Haul Group</span>
    </div>
    <div class="brand-rule"></div>
    <p class="services">Generators . Lighting Towers . De-watering Pumps . Compressors</p>
  </section>

  <section class="card card--back">
    <div class="brand">
      <span class="brand-mark"></span>
      <span class="brand-name">Silverpine Haul Group</span>
    </div>
    <div class="brand-rule"></div>
    <p class="person-name">Marek Oyelaran</p>
    <p class="person-role">Director</p>
    <div class="contact-icons">
      <span class="contact-icon" aria-label="Phone">
        <svg width="12" height="12" viewBox="0 0 24 24"><path fill="#fff" d="M6.6 10.8a15.1 15.1 0 0 0 6.6 6.6l2.2-2.2c.3-.3.7-.4 1-.2 1.1.4 2.3.6 3.6.6.6 0 1 .4 1 1V20c0 .6-.4 1-1 1C10.6 21 3 13.4 3 4c0-.6.4-1 1-1h3.5c.6 0 1 .4 1 1 0 1.3.2 2.5.6 3.6.1.3 0 .7-.2 1z"/></svg>
      </span>
      <span class="contact-icon" aria-label="Email">
        <svg width="12" height="12" viewBox="0 0 24 24"><rect x="2" y="5" width="20" height="14" rx="1.5" fill="#fff"/><path d="M3 6l9 7 9-7" fill="none" stroke="#e4a33a" stroke-width="2"/></svg>
      </span>
    </div>
    <p class="contact-line">0461527308</p>
    <p class="contact-line">silverpinehaulgroup@postvane.com</p>
  </section>
</main>
</body>
</html>
```